Redesign retirement planner website

Provide an original design for a website. The site should introduce the retirement planner, explain the basic offerings of his services, and invite the website visitor to enter their name, phone, and email. Please provide a ready-to-publish redesign that can actually be published via a Wordpress template or other major website builder like SquareSpace or Wix. Some introductory content is attached, but feel free to add additional sections/images/blocks/copywriting and rearrange/delete sections entirely to make your design original and compelling. Feel free to pull copywriting from here but again, do not use this original design, feel free to create an entirely NEW design and layout. lynx-mango-trel (dot) sitefolio (dot) com password: 1234 -- FINAL NOTE: Do not choose a stock photo of a man for the retirement planner. This website needs to work well with no photo of the retirement planner himself. Think of a non-face-focused design to win this competition.

Industry/Entity Type

Retirement planner personal website

Number of Pages Required

1 page

Font styles to use
Sans Serif
Decorative

Requirements
Must have
• Please provide a ready-to-publish redesign that can actually be published via a Wordpress template or other major website builder.

```html
<!DOCTYPE html>
<html lang="en">
<head>
<meta charset="utf-8">
<title>Marlon Keswick — Counselor &amp; Retirement Specialist</title>
<link rel="stylesheet" href="https://fonts.googleapis.com/css2?family=Abril+Fatface&family=Bodoni+Moda:wght@400&family=Roboto:wght@300;400;500;700&display=swap">
<style>
:root{
  --yellow:#fbbf0f;
  --gold:#f2ae00;
  --orange:#f29a1e;
  --orange-deep:#e8590c;
  --ink:#2b2424;
  --text:#333;
  --muted:#7a7370;
  --cream-a:#fdeec4;
  --cream-b:#fbdfb0;
  --peach:#fadcb8;
  --field:#fbdcb4;
  --footer:#3a2e2b;
  --white:#fff;
}
*{box-sizing:border-box;margin:0;padding:0}
html,body{width:1200px;height:3805px;overflow:hidden}
body{position:relative;background:var(--white);font-family:"Roboto",sans-serif;color:var(--text)}
.abs{position:absolute}
.display{font-family:"Abril Fatface",serif;font-weight:400}

/* header */
.site-header{left:0;top:0;width:1200px;height:67px;background:var(--white);box-shadow:0 2px 6px rgba(0,0,0,.12);z-index:5}
.brand{left:52px;top:15px;display:flex;align-items:center;gap:8px}
.brand-box{width:38px;height:38px;background:#111;border-radius:4px;color:var(--yellow);font-family:"Roboto",sans-serif;font-weight:700;font-size:16px;display:flex;align-items:center;justify-content:center}
.nav{top:22px;font-size:19px;color:#8a8a8a;display:flex;align-items:center}
.nav.home{left:547px;color:var(--orange);font-weight:500}
.nav svg{margin-left:10px}
.cta{left:992px;top:13px;width:156px;height:40px;border-radius:8px;background:var(--yellow);color:var(--ink);font-weight:700;font-size:15px;display:flex;align-items:center;justify-content:center;letter-spacing:.5px}

/* hero */
.hero-kicker{left:103px;top:226px;font-size:18px;color:var(--ink)}
.hero-title{left:103px;top:250px;font-size:64px;line-height:50px;color:var(--gold);letter-spacing:2px}
.hero-rule{left:108px;top:370px;width:3px;height:189px;background:#c9c4c0}
.hero-sub{left:123px;top:370px;font-size:22px;font-weight:300;color:var(--gold)}
.hero-copy{left:123px;top:445px;width:520px;font-size:17px;line-height:22.5px;color:var(--ink)}
.mark-art{background:radial-gradient(ellipse at 45% 45%,#f2a93a 0%,#e58b1f 55%,rgba(255,255,255,0) 72%);border-radius:40%}

/* specialties */
.specialties{left:0;top:780px;width:1200px;height:781px;background:linear-gradient(120deg,var(--cream-a),var(--cream-b))}
.section-label{font-size:22px;color:var(--muted)}
.spec-heading{left:99px;top:100px;font-size:66px;color:var(--ink);letter-spacing:1px}
.spec-item{width:372px}
.spec-title{display:flex;align-items:center;gap:26px;font-size:21px;color:var(--orange)}
.spec-desc{margin-top:10px;font-size:15px;line-height:18px;color:#4a4240}
.piggy-art{left:884px;top:572px;width:266px;height:180px;border-radius:50% 50% 20% 20%;background:linear-gradient(100deg,#f1a7c0 0%,#e68fae 55%,#c9b23d 70%,#d8c04a 100%)}

/* offerings */
.offer-label{left:0;top:1618px;width:1200px;text-align:center;font-size:22px;color:#f07a1a}
.offer-heading{left:0;top:1645px;width:1200px;text-align:center;font-size:70px;color:var(--orange-deep);letter-spacing:1px}
.offer-card{top:1812px;width:238px;height:241px;border:1.5px solid #555;border-radius:22px;background:var(--white);text-align:center}
.offer-card svg{position:absolute;left:50%;transform:translateX(-50%);top:40px}
.offer-name{position:absolute;left:0;right:0;top:128px;font-size:29px;line-height:36px;font-weight:500;color:var(--ink)}

/* faq */
.faq{left:0;top:2110px;width:1200px;height:780px;background:var(--peach);overflow:hidden}
.faq-heading{left:0;top:52px;width:1200px;text-align:center;font-size:68px;color:var(--ink)}
.faq-art{left:330px;top:250px;width:580px;height:340px;border-radius:45%;background:radial-gradient(ellipse at 55% 40%,rgba(232,140,30,.45) 0%,rgba(232,140,30,.25) 45%,rgba(250,220,184,0) 72%)}
.faq-item{left:194px;width:812px;background:rgba(255,248,240,.82);border-radius:12px}
.faq-q{position:absolute;left:28px;top:34px;font-size:20.5px;color:#3a3330}
.faq-item svg{position:absolute;right:24px;top:34px}
.faq-item.open{background:var(--white)}
.faq-item.open .faq-q{color:var(--orange);font-weight:500}
.faq-a{position:absolute;left:57px;top:96px;width:720px;font-size:14.5px;line-height:18px;color:#4a4240}

/* contact */
.contact-label{left:109px;top:3008px}
.contact-heading{left:109px;top:3034px;font-family:"Bodoni Moda",serif;font-weight:400;font-size:47px;color:var(--ink);letter-spacing:1px;white-space:nowrap}
.field{background:var(--field);border-radius:10px;height:57px;font-size:14.5px;color:#e99a4a;padding:20px 0 0 28px}
.check{left:109px;top:3389px;width:30px;height:30px;border:1.5px solid #f0a04a;border-radius:3px;background:var(--white)}
.check-label{left:150px;top:3394px;font-size:15px;color:var(--ink)}
.send{left:109px;top:3467px;width:349px;height:80px;border-radius:10px;background:var(--yellow);box-shadow:0 6px 12px rgba(0,0,0,.18);display:flex;align-items:center;justify-content:center;gap:18px;font-size:21px;font-weight:700;color:var(--ink)}

/* footer */
.footer-bar{left:0;top:3670px;width:1200px;height:10px;background:var(--yellow)}
.footer{left:0;top:3680px;width:1200px;height:125px;background:var(--footer)}
.footer-name{left:52px;top:16px;font-size:23px;color:var(--yellow);letter-spacing:1px}
.footer-line{left:52px;font-size:15px;color:var(--white);display:flex;align-items:center;gap:14px}
.social{left:1040px;top:44px;display:flex;align-items:center;gap:10px;font-size:17px;color:var(--yellow);font-weight:500}
.social-dot{width:36px;height:36px;border-radius:50%;background:var(--yellow)}
</style>
</head>
<body>

<header class="abs site-header">
  <div class="abs brand"><div class="brand-box">MK</div></div>
  <a class="abs nav home">Home</a>
  <a class="abs nav" style="left:627px">Specialties <svg width="16" height="10" viewBox="0 0 16 10"><path d="M1 1l7 7 7-7" fill="none" stroke="#8a8a8a" stroke-width="2"/></svg></a>
  <a class="abs nav" style="left:776px">Insurance Offers <svg width="16" height="10" viewBox="0 0 16 10"><path d="M1 1l7 7 7-7" fill="none" stroke="#8a8a8a" stroke-width="2"/></svg></a>
  <a class="abs cta">CONTACT ME</a>
</header>

<section class="hero">
  <p class="abs hero-kicker">I'm a</p>
  <h1 class="abs display hero-title">Counselor &amp;<br>Retirement Specialist</h1>
  <div class="abs hero-rule"></div>
  <p class="abs hero-sub">with a unique approach to financial planning.</p>
  <p class="abs hero-copy">You have a lifetime of accomplishments. Learning about them is my extraordinary honor. When I meet clients to make a plan for their final years of work and savings, I understand my solemn privilege. Your capital is irreplaceable. My job is to maximize its benefit for your health, family, and legacy.</p>
  <div class="abs mark-art" role="img" aria-label="Large 3D orange brand initial artwork" style="left:879px;top:466px;width:266px;height:244px"></div>
</section>

<section class="abs specialties">
  <p class="abs section-label" style="left:99px;top:72px">My specialties</p>
  <h2 class="abs display spec-heading">My specialties</h2>

  <div class="abs spec-item" style="left:126px;top:242px">
    <div class="spec-title">Estate Planning <svg width="28" height="28" viewBox="0 0 28 28"><path d="M12 3H3v22h22v-9M16 3h9v9M25 3L13 15" fill="none" stroke="#f29a1e" stroke-width="2.4"/></svg></div>
    <p class="spec-desc">Ensure your legacy is protected with comprehensive estate planning. I will guide you through creating wills, trusts, and other essential documents to secure your assets for future generations, ensuring your wishes are honored.</p>
  </div>
  <div class="abs spec-item" style="left:562px;top:242px">
    <div class="spec-title">Retirement Forecasting <svg width="28" height="28" viewBox="0 0 28 28"><path d="M12 3H3v22h22v-9M16 3h9v9M25 3L13 15" fill="none" stroke="#f29a1e" stroke-width="2.4"/></svg></div>
    <p class="spec-desc">Plan for a fulfilling retirement with our expert forecasting services. I will analyze your financial situation and future needs to develop a personalized strategy, helping you achieve your retirement goals with confidence.</p>
  </div>
  <div class="abs spec-item" style="left:126px;top:416px">
    <div class="spec-title">Final Expense <svg width="28" height="28" viewBox="0 0 28 28"><path d="M12 3H3v22h22v-9M16 3h9v9M25 3L13 15" fill="none" stroke="#f29a1e" stroke-width="2.4"/></svg></div>
    <p class="spec-desc">Prepare for life's final expenses with peace of mind. My services help you plan for costs associated with end-of-life arrangements, alleviating financial stress for your loved ones during a difficult time.</p>
  </div>
  <div class="abs spec-item" style="left:562px;top:416px">
    <div class="spec-title">Life Insurance <svg width="28" height="28" viewBox="0 0 28 28"><path d="M12 3H3v22h22v-9M16 3h9v9M25 3L13 15" fill="none" stroke="#f29a1e" stroke-width="2.4"/></svg></div>
    <p class="spec-desc">Safeguard your family's future with tailored life insurance solutions. I provide expert advice to help you choose the right coverage, ensuring financial security for your loved ones when they need it most.</p>
  </div>
  <div class="abs spec-item" style="left:126px;top:590px">
    <div class="spec-title">Portfolio Evaluation <svg width="28" height="28" viewBox="0 0 28 28"><path d="M12 3H3v22h22v-9M16 3h9v9M25 3L13 15" fill="none" stroke="#f29a1e" stroke-width="2.4"/></svg></div>
    <p class="spec-desc">Maximize your investment potential with our thorough portfolio evaluation. I assess your current assets and provide strategic recommendations to enhance your financial growth and stability.</p>
  </div>

  <div class="abs piggy-art" role="img" aria-label="Pink piggy bank beside a stack of gold coins"></div>
</section>

<section class="offerings">
  <p class="abs offer-label">Insurance</p>
  <h2 class="abs display offer-heading">Offerings</h2>

  <div class="abs offer-card" style="left:152px">
    <svg width="48" height="50" viewBox="0 0 48 50"><circle cx="20" cy="12" r="10" fill="#3d3535"/><path d="M2 46c0-14 8-22 18-22s18 8 18 22z" fill="#3d3535"/><circle cx="35" cy="35" r="11" fill="#3d3535" stroke="#fff" stroke-width="3"/></svg>
    <p class="offer-name">Whole and<br>Universal Life</p>
  </div>
  <div class="abs offer-card" style="left:480px">
    <svg width="56" height="40" viewBox="0 0 56 40"><circle cx="16" cy="22" r="15" fill="#3d3535"/><g fill="#3d3535"><rect x="28" y="2" width="26" height="5" rx="2"/><rect x="32" y="10" width="22" height="5" rx="2"/><rect x="33" y="18" width="21" height="5" rx="2"/><rect x="32" y="26" width="22" height="5" rx="2"/><rect x="28" y="34" width="26" height="5" rx="2"/></g></svg>
    <p class="offer-name">Annuities</p>
  </div>
  <div class="abs offer-card" style="left:810px">
    <svg width="52" height="52" viewBox="0 0 52 52"><rect x="2" y="6" width="44" height="36" rx="4" fill="#3d3535"/><rect x="10" y="1" width="5" height="9" rx="2" fill="#3d3535"/><rect x="33" y="1" width="5" height="9" rx="2" fill="#3d3535"/><rect x="2" y="14" width="44" height="3" fill="#fff"/><circle cx="38" cy="38" r="12" fill="#fff" stroke="#3d3535" stroke-width="3"/><text x="38" y="44" font-size="16" text-anchor="middle" font-family="Roboto,sans-serif" font-weight="700" fill="#3d3535">$</text></svg>
    <p class="offer-name">Term and<br>Final Expense</p>
  </div>
</section>

<section class="abs faq">
  <h2 class="abs display faq-heading">FAQs</h2>
  <div class="abs faq-art" role="img" aria-label="Faint large brand initial artwork in the background"></div>

  <div class="abs faq-item" style="top:169px;height:93px">
    <p class="faq-q">Why is portfolio evaluation important for retirement planning?</p>
    <svg width="16" height="26" viewBox="0 0 16 26"><path d="M2 2l11 11L2 24" fill="none" stroke="#f29a1e" stroke-width="2.5"/></svg>
  </div>
  <div class="abs faq-item" style="top:283px;height:93px">
    <p class="faq-q">What are final expenses and why should I plan for them?</p>
    <svg width="16" height="26" viewBox="0 0 16 26"><path d="M2 2l11 11L2 24" fill="none" stroke="#f29a1e" stroke-width="2.5"/></svg>
  </div>
  <div class="abs faq-item open" style="top:397px;height:170px">
    <p class="faq-q">How does retirement forecasting help me plan for the future?</p>
    <svg width="28" height="18" viewBox="0 0 28 18"><path d="M2 3l12 12L26 3" fill="none" stroke="#f29a1e" stroke-width="2.5"/></svg>
    <p class="faq-a">Retirement forecasting analyzes your current financial situation, expected income, and future needs to create a personalized strategy. This ensures you can meet your retirement goals with confidence and enjoy financial security throughout your retirement years.</p>
  </div>
  <div class="abs faq-item" style="top:587px;height:93px">
    <p class="faq-q">What is the difference between Whole Life and Universal Life Insurance?</p>
    <svg width="16" height="26" viewBox="0 0 16 26"><path d="M2 2l11 11L2 24" fill="none" stroke="#f29a1e" stroke-width="2.5"/></svg>
  </div>
</section>

<section class="contact">
  <p class="abs section-label contact-label" style="font-size:19px">Contact Me</p>
  <h2 class="abs contact-heading">Allow me to introduce myself.</h2>
  <div class="abs field" style="left:109px;top:3142px;width:292px">First Name</div>
  <div class="abs field" style="left:424px;top:3142px;width:374px">Last Name</div>
  <div class="abs field" style="left:109px;top:3223px;width:689px">Email</div>
  <div class="abs field" style="left:109px;top:3303px;width:374px">Phone</div>
  <div class="abs check"></div>
  <p class="abs check-label">Sign up for news and updates</p>
  <a class="abs send">SEND A MESSAGE <svg width="20" height="15" viewBox="0 0 20 15"><rect width="20" height="15" rx="2" fill="#2b2424"/><path d="M1 2l9 6 9-6" fill="none" stroke="#fbbf0f" stroke-width="1.6"/></svg></a>
  <div class="abs mark-art" role="img" aria-label="Large 3D orange brand initial artwork" style="left:850px;top:3325px;width:266px;height:237px"></div>
</section>

<div class="abs footer-bar"></div>
<footer class="abs footer">
  <p class="abs display footer-name">Marlon Keswick</p>
  <p class="abs footer-line" style="top:58px"><svg width="16" height="12" viewBox="0 0 16 12"><rect width="16" height="12" rx="1.5" fill="#fff"/><path d="M1 1.5l7 5 7-5" fill="none" stroke="#3a2e2b" stroke-width="1.4"/></svg>mkeswick@harborplan.net</p>
  <p class="abs footer-line" style="top:84px"><svg width="16" height="16" viewBox="0 0 16 16"><path d="M3 1l3 3-2 2c1 2 3 4 5 5l2-2 3 3-2 3C7 15 1 9 1 3z" fill="#fff"/></svg>(555) 014 - 0188</p>
  <div class="abs social"><span class="social-dot"></span>Linkio</div>
</footer>

</body>
</html>
```